Overseas Property Tax Depreciation

We need a two sided flyer to promote our business and explain what we do. our website is www.tolbexmu.net.
The attached word file is what I would like on an A5 size flyer with one side showing the FAQ and the other the worked example. I would like these formatted much better than the are and in general style of the website. I will attach files for logos as well.

```html
<!DOCTYPE html>
<html lang="en">
<head>
<meta charset="utf-8">
<title>Farshore Tax Depreciation – Flyer</title>
<link href="https://fonts.googleapis.com/css2?family=Arimo:wght@400;700&family=Roboto+Condensed:wght@400;700&family=Roboto+Slab:wght@800&display=swap" rel="stylesheet">
<style>
:root{
  --bg:#4a3526;
  --paper:#ffffff;
  --green:#1f9a4a;
  --green-dark:#14843b;
  --green-table:#22a04c;
  --orange:#f7a21b;
  --yellow:#fbd63a;
  --grey-text:#555555;
  --title:#333333;
  --soft:#efefef;
}
*{box-sizing:border-box;margin:0;padding:0}
html,body{width:1200px;height:867px;overflow:hidden}
body{background:var(--bg);position:relative;font-family:"Arimo",Arial,sans-serif}
.page{position:absolute;top:79px;height:718px;background:var(--paper);overflow:hidden}
.page--back{left:75px;width:506px}
.page--front{left:606px;width:513px}

/* back */
.example-title{text-align:center;font-family:"Roboto Condensed",Arial Narrow,sans-serif;font-weight:700;color:#666;font-size:23px;margin-top:20px;line-height:26px}
.example-subtitle{text-align:center;font-family:"Roboto Condensed",Arial Narrow,sans-serif;font-weight:700;color:#666;font-size:19px;line-height:24px}
.calc{position:absolute;left:23px;top:83px;width:464px;border-collapse:collapse;color:#fff;font-size:10px;table-layout:fixed}
.calc th{background:var(--orange);font-family:"Roboto Condensed",sans-serif;font-weight:400;font-size:12px;line-height:12px;text-align:left;padding:0 6px;border-left:1px solid #fff}
.calc th:first-child{border-left:none;border-top-left-radius:8px}
.calc th.with{border-top-right-radius:8px;text-align:center}
.calc th.cur{font-size:11px;height:16px;text-align:center;border-top:1px solid #fff}
.calc td{background:var(--green-table);padding:0 5px;vertical-align:middle;border-left:1px solid #fff;line-height:12px;white-space:nowrap}
.calc td:first-child{border-left:none}
.calc tr.rule td{border-top:1px solid #fff}
.calc .note{font-style:italic;float:right}
.calc .b{font-weight:700}
.calc tr:last-child td:first-child{border-bottom-left-radius:8px}
.calc tr:last-child td:last-child{border-bottom-right-radius:8px}
.calc .big{font-size:14px;font-weight:700}
.back-tagline{position:absolute;left:0;width:100%;top:603px;text-align:center;color:var(--orange);font-family:"Roboto Condensed",sans-serif;font-size:13.5px}
.back-footer{position:absolute;top:635px;left:24px;right:20px;height:70px;display:flex;align-items:center}
.brand{display:flex;align-items:center;gap:7px;color:var(--green);font-family:"Roboto Condensed",sans-serif;font-weight:700}
.brand-dot{width:14px;height:14px;border-radius:50%;background:var(--orange);flex:none}
.back-footer .brand{font-size:18px;width:170px}
.contact-block{border-left:1px solid #ccc;padding-left:7px;margin-left:4px;font-size:8.5px;line-height:12px;color:#444;width:130px}
.partner-badge{width:90px;height:34px;border-radius:4px;background:#5a3d86;margin-left:12px}
.reg-seal{margin-left:18px;text-align:center;font-size:6px;color:#444}
.reg-seal span{display:block;width:44px;height:44px;border-radius:50%;border:3px solid #333;margin:0 auto 2px;background:#fff}

/* front */
.front-header{height:113px;display:flex;align-items:center;padding-left:26px}
.front-header .brand{font-size:26px;width:200px}
.front-title{border-left:1px solid #bbb;margin-left:24px;padding-left:22px;height:70px;font-family:"Roboto Slab",serif;font-weight:800;color:var(--title);font-size:26px;line-height:35px;white-space:nowrap;letter-spacing:-0.3px}
.contact-bar{height:27px;background:var(--green-dark);display:flex;align-items:center;color:#fff;font-family:"Roboto Condensed",sans-serif;font-weight:700;font-size:14px;padding-left:26px;gap:42px}
.contact-bar .item{display:flex;align-items:center;gap:6px}
.contact-bar .phone{font-size:20px}
.why{height:260px;background:linear-gradient(#fff,var(--soft));padding:16px 26px 0;color:var(--grey-text);font-size:8.3px;line-height:11px}
.why h2{font-size:15px;color:#555;font-weight:700;margin-bottom:9px}
.cols{display:flex;gap:14px}
.cols>div{flex:1}
.why p{text-align:justify;margin-bottom:12px}
.ticks{list-style:none}
.ticks li{display:flex;gap:6px;margin-bottom:7px;text-align:justify}
.ticks svg{flex:none;margin-top:0}
.faq{position:absolute;top:400px;left:0;right:0;bottom:0;background:var(--green);padding:8px 22px 0 22px;color:#fff;font-size:8.3px;line-height:11px}
.faq h3{color:var(--yellow);font-size:11.5px;line-height:14px;font-weight:700;margin:0 0 6px}
.faq p{text-align:justify;margin-bottom:9px}
.faq .cols{gap:22px}
.faq .ticks li{margin-bottom:3px}
</style>
</head>
<body>

<section class="page page--back">
  <h1 class="example-title">Property Tax Depreciation Example</h1>
  <p class="example-subtitle">3 bed Semi - detached house Dublin, Constructed in 2006</p>

  <table class="calc">
    <colgroup><col style="width:30px"><col style="width:256px"><col style="width:50px"><col style="width:50px"><col style="width:78px"></colgroup>
    <thead>
      <tr style="height:46px"><th rowspan="2">Ref</th><th rowspan="2">Description</th><th colspan="2" style="text-align:center">Without Property<br>Tax Depreciation</th><th class="with">With Property<br>Depreciation<br>Report</th></tr>
      <tr><th class="cur">Euro</th><th class="cur">AUD</th><th class="cur">AUD</th></tr>
    </thead>
    <tbody>
      <tr class="rule" style="height:22px"><td>A</td><td>Rental Income <span class="note" style="font-style:normal;margin-right:14px">€1,200 Month</span></td><td>€14,400</td><td>$20,571</td><td>$20,571</td></tr>
      <tr class="rule" style="height:52px"><td>B.</td><td>Expenses<br><br>Annual Interest charged on<br>outstanding Mortgage (4% apr)</td><td><br><br><br>€12,040</td><td><br><br><br>$17,200</td><td><br><br><br>$17,200</td></tr>
      <tr style="height:20px"><td>C</td><td>Property agent fees or commission</td><td>€1,200</td><td>$1,714</td><td>$1,714</td></tr>
      <tr style="height:21px"><td>D</td><td>Local Property Tax</td><td>€250</td><td>$357</td><td>$357</td></tr>
      <tr style="height:21px"><td>E</td><td>Repairs and Maintenance</td><td>€2,000</td><td>$2,857</td><td>$2,857</td></tr>
      <tr style="height:19px"><td>F</td><td>Home Insurance</td><td>€450</td><td>$643</td><td>$643</td></tr>
      <tr style="height:19px"><td>G</td><td>Cleaning Advertising et..</td><td>€1,500</td><td>$2,143</td><td>$2,143</td></tr>
      <tr style="height:20px" class="b"><td>H</td><td>Property Tax Depreciation</td><td>€0</td><td>$0</td><td>$15,000</td></tr>
      <tr class="rule b" style="height:20px"><td>I</td><td>Total Annual Expenses <span class="note" style="font-weight:400;margin-right:10px">Total (B to H)</span></td><td>€17,440</td><td>$24,914</td><td>$39,914</td></tr>
      <tr class="rule b" style="height:20px"><td>J</td><td>Annual Rental Loss/Gain <span class="note" style="font-weight:400;margin-right:60px">(A less I)</span></td><td>-€3,040</td><td>-$4,343</td><td>-$19,343</td></tr>
      <tr class="rule" style="height:21px"><td>K</td><td>Your Annual Income from other sources</td><td></td><td>$180,000</td><td>$180,000L</td></tr>
      <tr style="height:32px"><td>L</td><td>Tour Taxable Income after <span class="note" style="margin-right:60px">(K Plus J)</span><br>Rental Losses/Gains</td><td></td><td>$175,657</td><td>$160,657</td></tr>
      <tr style="height:36px"><td>M</td><td>Your Marginal Income Tax Rate<br>(37% +2% medicare) <span class="note b" style="font-style:normal;margin-right:20px">39%</span></td><td></td><td></td><td></td></tr>
      <tr class="rule" style="height:36px"><td>N</td><td>Annual Tax Saving <span class="note" style="margin-right:30px">(J multiplied by M)</span><br>Foreign Tax Credits</td><td></td><td>$1,694</td><td>$7,544</td></tr>
      <tr style="height:36px"><td>O</td><td>Non-resident Landlord withholding Tax <i>(20% Ireland)</i><br><i>(A multiplied by 20%)</i></td><td><br>€2,880</td><td><br>$4,114</td><td><br>$4,114</td></tr>
      <tr style="height:18px" class="b"><td>P</td><td>Nett Tax Savings <span class="note" style="font-weight:400;margin-right:60px">(N Plus O)</span></td><td>$5,808</td><td>$11,658</td><td></td></tr>
      <tr class="rule b" style="height:40px"><td>Q</td><td>Additional Money in your Pocket (Australia)<br>per year due to Property Tax Depreciation</td><td></td><td colspan="2" class="big" style="border-left:1px solid #fff">&nbsp;&nbsp;$5,850</td></tr>
    </tbody>
  </table>

  <p class="back-tagline">TAX DEPRECIATION REPORTS FOR AUSTRALIAN PROPERTIES</p>

  <div class="back-footer">
    <div class="brand"><span class="brand-dot"></span>Farshore Tax Depreciation</div>
    <div class="contact-block">Suite 000, City name,<br>Country name 00000.<br><b>Tel:</b> 000 000 0000<br><b>email:</b> hello@farshore.com</div>
    <div class="partner-badge" role="img" aria-label="Professional body membership badge"></div>
    <div class="reg-seal"><span role="img" aria-label="Registered tax practitioner seal"></span>Tax agent<br>31620745</div>
  </div>
</section>

<section class="page page--front">
  <header class="front-header">
    <div class="brand"><span class="brand-dot"></span>Farshore Tax Depreciation</div>
    <h1 class="front-title">PROPERTY TAX<br>DEPRECIATION</h1>
  </header>
  <div class="contact-bar">
    <span class="item">www.tolbexmu.net</span>
    <span class="item"><svg width="20" height="13" viewBox="0 0 20 13"><rect x="0.5" y="0.5" width="19" height="12" fill="#fff"/><path d="M1 1l9 7 9-7" fill="none" stroke="#14843b" stroke-width="1.2"/></svg>info@farshoretax.com</span>
    <span class="item phone"><svg width="18" height="18" viewBox="0 0 18 18"><circle cx="9" cy="9" r="8" fill="none" stroke="#fff" stroke-width="1.5"/><path d="M6 5l2 2-1 1.5c.6 1.3 1.2 1.9 2.5 2.5L11 10l2 2-1.5 1.5C8.5 13 5 9.5 4.5 6z" fill="#fff"/></svg>31 62 07 45</span>
  </div>

  <div class="why">
    <h2>Why use us?</h2>
    <div class="cols">
      <div>
        <p>There are several websites out there offering tax depreciation reports for Australian properties but there are very few who are appropriately qualified and approved by the Australian Tax Office (ATO) and offer the necessary Irish expertise. The Quantity Surveyor that prepares your report:</p>
        <ul class="ticks">
          <li><svg width="10" height="10" viewBox="0 0 10 10"><rect x=".5" y=".5" width="9" height="9" fill="#fff" stroke="#999"/><path d="M2 5l2 2 5-6" fill="none" stroke="#e8a21b" stroke-width="1.6"/></svg>is Irish and qualified as a Quantity Surveyor in Ireland.</li>
          <li><svg width="10" height="10" viewBox="0 0 10 10"><rect x=".5" y=".5" width="9" height="9" fill="#fff" stroke="#999"/><path d="M2 5l2 2 5-6" fill="none" stroke="#e8a21b" stroke-width="1.6"/></svg>worked there during the "Celtic Tiger" period when construction costs were quite high.</li>
          <li><svg width="10" height="10" viewBox="0 0 10 10"><rect x=".5" y=".5" width="9" height="9" fill="#fff" stroke="#999"/><path d="M2 5l2 2 5-6" fill="none" stroke="#e8a21b" stroke-width="1.6"/></svg>has detailed knowledge of Irish construction methods and costs over the past 20 years. Irish buildings are generally much more expensive than Australia due to the climate, just think about how many Australian houses you have seen that have double glazing, central heating, insulation etc..</li>
        </ul>
      </div>
      <div>
        <ul class="ticks">
          <li><svg width="10" height="10" viewBox="0 0 10 10"><rect x=".5" y=".5" width="9" height="9" fill="#fff" stroke="#999"/><path d="M2 5l2 2 5-6" fill="none" stroke="#e8a21b" stroke-width="1.6"/></svg>has a partnership arrangement with an Irish quantity surveying firm to carry out the property inspections required in most cases to maximize the deductions available.</li>
          <li><svg width="10" height="10" viewBox="0 0 10 10"><rect x=".5" y=".5" width="9" height="9" fill="#fff" stroke="#999"/><path d="M2 5l2 2 5-6" fill="none" stroke="#e8a21b" stroke-width="1.6"/></svg>is a chartered member of the RSVA.</li>
          <li><svg width="10" height="10" viewBox="0 0 10 10"><rect x=".5" y=".5" width="9" height="9" fill="#fff" stroke="#999"/><path d="M2 5l2 2 5-6" fill="none" stroke="#e8a21b" stroke-width="1.6"/></svg>Maintains the Appropriate Professional Indemnity Insurance.</li>
          <li><svg width="10" height="10" viewBox="0 0 10 10"><rect x=".5" y=".5" width="9" height="9" fill="#fff" stroke="#999"/><path d="M2 5l2 2 5-6" fill="none" stroke="#e8a21b" stroke-width="1.6"/></svg>Is registered with the Tax Practitioners Board. All quantity surveyors who prepare Property Tax Depreciation Schedules are required by the ATO to be registered with the Tax Practitioners Board which checks that the person preparing the reports is suitably qualified and maintains the appropriate professional indemnity insurance. You can check the registration on the TPB website. Our registration number is 31620745.</li>
        </ul>
      </div>
    </div>
  </div>

  <div class="faq">
    <div class="cols">
      <div>
        <h3>My property is in Ireland does this make a difference?</h3>
        <p>Division 43 of the Income Tax Assessment Act 1997 which deals with capital works depreciation states that it applies to buildings begun outside Australia after 21 August 1990 Sect 43.20 (1) (b). Your Australian tax return should cover your worldwide income. As long as the property is available to rent back in Ireland you are obliged by the ATO to report any income or loss on that property.</p>
        <h3>Is my property too old?</h3>
        <p>No, if your property was constructed after 1990 you can claim for both the construction cost element and the Plant and equipment. If it was built before then you can still claim the plant and equipment allowance. The easiest thing to do is to contact us with some details on your property and we can make an initial assessment of the possible annual savings.</p>
        <h3>What is Property Depreciation?</h3>
        <p>Just like you claim wear and tear on a car purchased for income producing purposes, you can also claim the depreciation of your investment property against your taxable income.</p>
      </div>
      <div>
        <p>There are 2 types available: depreciation on Plant and Equipment, and depreciation on the cost of construction. Plant and Equipment refers to items within the building like ovens, dishwashers, carpet and blinds etc. Both these costs can be offset against your assessable income.</p>
        <h3>How much will the report cost?</h3>
        <p>Each scenario is different so contact us to obtain a quick quote for your situation. Generally the cost of the report is a fraction of the savings in any one year.</p>
        <ul class="ticks">
          <li><svg width="10" height="10" viewBox="0 0 10 10"><rect x=".5" y=".5" width="9" height="9" fill="#fff" stroke="#999"/><path d="M2 5l2 2 5-6" fill="none" stroke="#e8a21b" stroke-width="1.6"/></svg>Our fee is fully tax deductible</li>
          <li><svg width="10" height="10" viewBox="0 0 10 10"><rect x=".5" y=".5" width="9" height="9" fill="#fff" stroke="#999"/><path d="M2 5l2 2 5-6" fill="none" stroke="#e8a21b" stroke-width="1.6"/></svg>You do NOT need to get this report done every year so the cost can be spread over several years</li>
        </ul>
        <h3 style="margin-top:8px">I haven't included my property for the past couple of years on my tax return is this a problem?</h3>
        <p>No, in actual fact you could have been missing out on savings for a number of years, you can also use this report to claim a refund from the ATO for up to the past three years.</p>
      </div>
    </div>
  </div>
</section>

</body>
</html>
```